KMT Law Firm Business Card

We need a business card design for our law firm. We recently had a name change and so we have a new logo. We are a small plaintiff's law firm in Oklahoma but do work all over the USA We have a new logo (see attached the artwork in both black & brown – could also reverse the logo so that it’s white) We'd like an upscale western design. One side needs the logo and this slogan : "Integrity-Grit-Resolve Always stand your ground"
and on the other side needs to be a template so we can fill in the attorney's name --include this info:
Whitcombe Whitcombe Delacroix
-------Attorneys------------
(name of attorney) ie: Howard T. Whitcombe
(title) ie: Attorney/Managing Partner
5812 S. Garnet Tulsa, OK 74139
918-555-0143
Fax 918-555-0178
(name)@kmtlegal.example www.kmtlegal.example ie: hank@kmtlegal.example
also needs a small Facebook & twitter logo -
and 3 of the attorneys need the circle logo attached that says "Grand Verdict Litigators Circle" - so we need to be able to remove that for some of the designs –

Industry/Entity Type

Law Firm

```html
<!DOCTYPE html>
<html lang="en">
<head>
<meta charset="utf-8">
<title>Whitcombe Whitcombe Delacroix – Business Card</title>
<link href="https://fonts.googleapis.com/css2?family=Roboto:wght@400;500&display=swap" rel="stylesheet">
<style>
  :root {
    --page-bg: #d9d9d9;
    --card-dark: #2b2b2b;
    --card-light: #e9e9e9;
    --ink-light: #ffffff;
    --ink-dark: #1e1e1e;
    --ink-muted: #555555;
    --rule: #8a8a8a;
  }
  * { margin: 0; padding: 0; box-sizing: border-box; }
  html, body { width: 1200px; height: 1000px; overflow: hidden; }
  body {
    background: var(--page-bg);
    font-family: "Roboto", Arial, sans-serif;
    position: relative;
  }
  .card {
    position: absolute;
    left: 250px;
    width: 700px;
    height: 400px;
    box-shadow: 0 6px 18px rgba(0,0,0,0.25);
  }
  .card--front { top: 70px; background: var(--card-dark); color: var(--ink-light); }
  .card--back  { top: 530px; background: var(--card-light); color: var(--ink-dark); }

  .firm-mark {
    display: flex;
    align-items: center;
    gap: 14px;
    font-weight: 500;
    letter-spacing: 0.06em;
    text-transform: uppercase;
  }
  .firm-mark__dot {
    border: 2px solid currentColor;
    border-radius: 50%;
    flex: none;
  }

  .card--front .firm-mark {
    position: absolute;
    top: 120px;
    right: 60px;
    font-size: 20px;
  }
  .card--front .firm-mark__dot { width: 34px; height: 34px; }
  .slogan {
    position: absolute;
    top: 240px;
    left: 70px;
    font-size: 24px;
    font-weight: 400;
  }

  .card--back .firm-mark {
    position: absolute;
    top: 60px;
    left: 40px;
    width: 250px;
    font-size: 15px;
    line-height: 1.35;
  }
  .card--back .firm-mark__dot { width: 26px; height: 26px; }
  .divider {
    position: absolute;
    top: 40px;
    bottom: 40px;
    left: 320px;
    width: 1px;
    background: var(--rule);
  }
  .details {
    position: absolute;
    top: 40px;
    left: 350px;
    right: 30px;
  }
  .details__name { font-size: 26px; font-weight: 500; }
  .details__title { font-size: 19px; color: var(--ink-muted); margin-top: 4px; }
  .contact-list { list-style: none; margin-top: 22px; }
  .contact-list li {
    display: flex;
    align-items: center;
    gap: 12px;
    font-size: 19px;
    color: var(--ink-muted);
    margin-bottom: 8px;
  }
  .contact-list svg { width: 18px; height: 18px; flex: none; }
  .address {
    position: absolute;
    left: 40px;
    bottom: 40px;
    font-size: 19px;
    color: var(--ink-muted);
    line-height: 1.35;
  }
</style>
</head>
<body>
  <section class="card card--front" aria-label="Business card front">
    <div class="firm-mark"><span class="firm-mark__dot"></span>Whitcombe Whitcombe Delacroix</div>
    <p class="slogan">Integrity-Grit-Resolve Always stand your ground</p>
  </section>

  <section class="card card--back" aria-label="Business card back">
    <div class="firm-mark"><span class="firm-mark__dot"></span><span>Whitcombe Whitcombe Delacroix</span></div>
    <div class="divider"></div>
    <div class="details">
      <h1 class="details__name">Howard T. Whitcombe</h1>
      <p class="details__title">Managing Partner</p>
      <ul class="contact-list">
        <li>
          <svg viewBox="0 0 20 20" aria-hidden="true"><path d="M4 2h4l1 4-2 2a11 11 0 0 0 5 5l2-2 4 1v4a2 2 0 0 1-2 2A16 16 0 0 1 2 4a2 2 0 0 1 2-2z" fill="#333"/></svg>
          918-555-0143
        </li>
        <li>
          <svg viewBox="0 0 20 20" aria-hidden="true"><rect x="5" y="2" width="10" height="5" fill="#333"/><rect x="2" y="7" width="16" height="7" rx="1" fill="#333"/><rect x="5" y="12" width="10" height="6" fill="#fff" stroke="#333" stroke-width="1.5"/></svg>
          918-555-0178
        </li>
        <li>
          <svg viewBox="0 0 20 20" aria-hidden="true"><rect x="2" y="4" width="16" height="12" fill="#333"/><path d="M2 4l8 7 8-7" fill="none" stroke="#fff" stroke-width="1.5"/></svg>
          hank@kmtlegal.example
        </li>
        <li>
          <svg viewBox="0 0 20 20" aria-hidden="true"><rect x="3" y="3" width="14" height="14" fill="none" stroke="#333" stroke-width="1.8"/></svg>
          www.kmtlegal.example
        </li>
      </ul>
    </div>
    <p class="address">5812 S. Garnet Tulsa<br>OK 74139</p>
  </section>
</body>
</html>
```